Korvenna Building Inspections, Estimating & Project Management

Please read my capability statement uploaded in the files to get an indepth overview of who we are and what we do.
We are a construction company that is moving away from onsite construction to consultancy and inspection services. We will offer Building Inspections, Estimating Services, Project Management and Construction Management. We will still be working out in the field, however as inspectors and and coordinators only.
I am looking to build a website from scratch. I already have my logo built by pixel harbour previously and wish to remove the company slogan "Structures & Buildworks".
Background: Korvenna Pty Ltd is in the process of shutting down and re-registering as Korvenna Australia Pty Ltd. It will however retain all the original logos.
I do like websites like https://zenith.plorvatic-sample.com/#
I also do like to write all my emails in Roboto-Light font and open to suggestions on it's usage.
I currently host with Southland Webhosts and they use Wordpress 5.0

Target Market(s)

Home Owners Building or Renovating, Realestate Agents, Commercial Builders, Trades that require Estimating,

Industry/Entity Type

Construction

Coding

Number of Pages Required

Font styles to use
Other font styles liked:
• All fonts have been uploaded.

Requirements
Must have
• Must have the ability for monthly updates, photo uploads and industry tips I can share. A page dedicated to tips and understanding of what sets us apart from the competitors (this will require lots of input from me).
Nice to have
• I personally like pages like https://zenith.plorvatic-sample.com/# which have a background image and the foreground scrolling past. Open to suggestions here. A website that sets me apart of Brisbane rivals
Should not have
• Fixed pricing

```html
<!DOCTYPE html>
<html lang="en">
<head>
<meta charset="utf-8">
<title>Korvenna Australia – Building Inspections, Estimating & Project Management</title>
<link href="https://fonts.googleapis.com/css2?family=Roboto:wght@300;400;500;700;900&display=swap" rel="stylesheet">
<style>
:root{
  --yellow:#fdb913;
  --ink:#1c1c1c;
  --text:#4a4a4a;
  --muted:#6b6b6b;
  --line:#ececec;
  --dark:#222222;
  --white:#ffffff;
  --faint:#eeeeee;
}
*{box-sizing:border-box;margin:0;padding:0}
html,body{width:1200px;height:2882px;overflow:hidden;background:var(--white)}
body{position:relative;font-family:'Roboto',sans-serif;color:var(--ink)}
.abs{position:absolute}
.eyebrow{font-size:10px;color:var(--yellow);font-weight:500}
.heading{font-size:14px;font-weight:700;color:var(--ink);line-height:18px}
.rule{width:35px;height:2px;background:var(--yellow)}
.para{font-size:9.5px;line-height:15px;color:var(--text);font-weight:300}
.btn{display:flex;align-items:center;justify-content:center;font-size:7.5px;font-weight:500;letter-spacing:.3px;text-transform:uppercase;height:24px}
.btn-yellow{background:var(--yellow);color:var(--ink)}
.btn-dark{background:var(--dark);color:var(--white)}
.divider{left:181px;width:838px;height:1px;background:var(--line)}

/* intro */
.intro-title{font-size:14px;font-weight:700;line-height:18px}
.intro-bar{width:2px;height:50px;background:var(--yellow)}

/* services */
.card{width:196px;height:143px;background:var(--white);box-shadow:0 0 6px rgba(0,0,0,.09);display:flex;flex-direction:column;align-items:center;justify-content:center;text-align:center}
.card-icon{width:50px;height:50px;border-radius:50%;background:var(--yellow);display:flex;align-items:center;justify-content:center;margin-bottom:12px}
.card-title{font-size:10px;font-weight:700;line-height:16px}
.card-text{font-size:8px;line-height:12.5px;color:var(--muted);width:160px;margin-bottom:16px}

/* photos */
.photo{background:linear-gradient(135deg,#4f78b8 0%,#9c5a3f 45%,#b56b4c 70%,#d9d2a0 100%)}
.photo-alt{background:linear-gradient(120deg,#3d6aa8 0%,#6a4a3a 40%,#b56b4c 75%,#e1d8b2 100%)}
.framed{border:3px solid var(--white);box-shadow:0 0 4px rgba(0,0,0,.1)}
.wordmark{font-size:30px;font-weight:900;color:var(--faint);letter-spacing:1px}

/* stats */
.stats-band{left:0;top:1520px;width:1200px;height:287px;background:linear-gradient(100deg,#4a3a2a 0%,#2d2620 40%,#3a3128 70%,#22201e 100%)}
.stat{width:174px;height:136px;border:1.5px solid var(--yellow);display:flex;flex-direction:column;align-items:center;justify-content:center}
.stat-num{font-size:40px;font-weight:900;color:var(--yellow);line-height:44px}
.stat-label{font-size:9.5px;font-weight:500;color:var(--white);margin-top:6px;text-transform:uppercase}

/* why */
.bullets{list-style:none}
.bullets li{position:relative;padding-left:13px;font-size:9.5px;color:var(--text);font-weight:300;height:21.8px}
.bullets li::before{content:"";position:absolute;left:0;top:3px;width:6px;height:6px;border-radius:50%;background:var(--yellow)}
.badge{width:112px;height:112px;border-radius:50%;background:var(--white);box-shadow:0 0 8px rgba(0,0,0,.15);display:flex;align-items:center;justify-content:center;font-size:12px;font-weight:700;color:var(--ink)}

/* partners */
.partners-band{left:0;top:2354px;width:1200px;height:290px;background:var(--dark)}
.partner{width:152px;height:89px;background:#141414;display:flex;align-items:center;justify-content:center;color:var(--white);font-size:13px;font-weight:500;letter-spacing:.5px}
.dot{width:6px;height:6px;border-radius:50%;background:#777}
.dot.on{background:var(--white)}

/* cta */
.cta{left:181px;top:2593px;width:838px;height:112px;background:var(--yellow)}

/* footer */
.f-label{font-size:8.5px;color:var(--muted)}
.f-value{font-size:9.5px;color:var(--ink)}
.copyright{left:0;width:1200px;text-align:center;font-size:8.5px;color:var(--muted)}
</style>
</head>
<body>

<!-- Intro -->
<header>
  <div class="abs eyebrow" style="left:181px;top:62px">Korvenna Australia</div>
  <h1 class="abs intro-title" style="left:181px;top:80px;width:220px">Building Inspections, Estimating &amp; Project Management</h1>
  <div class="abs intro-bar" style="left:427px;top:64px"></div>
  <p class="abs para" style="left:467px;top:65px;width:545px;font-size:10px;line-height:16.5px">Korvenna Australia leads the industry in high-quality building inspections, estimating &amp; project management. With a proven track record of over 1,200 completed projects, we deliver precise, efficient, and customized solutions for residential &amp; commercial clients.</p>
</header>
<div class="abs divider" style="top:151px"></div>

<!-- Services -->
<section>
  <svg width="0" height="0" style="position:absolute">
    <symbol id="ico-building" viewBox="0 0 30 30">
      <g fill="none" stroke="#1c1c1c" stroke-width="1.4">
        <rect x="5" y="9" width="13" height="17"/>
        <path d="M18 14h7v12h-7"/>
        <path d="M8 9V5h7v4"/>
        <path d="M8 13h2M13 13h2M8 17h2M13 17h2M8 21h2M13 21h2M21 18h2M21 22h2"/>
        <path d="M3 26h24"/>
      </g>
    </symbol>
  </svg>

  <div class="abs card" style="left:181px;top:190px"><div class="card-icon"><svg width="30" height="30"><use href="#ico-building"/></svg></div><div class="card-title">Building &amp;<br>Pest Inspections</div></div>
  <div class="abs card" style="left:395px;top:190px"><p class="card-text">Building &amp; pest inspections assess structural integrity &amp; pest issues, ensuring informed property decisions.</p><div class="btn btn-yellow" style="width:76px">View More</div></div>
  <div class="abs card" style="left:609px;top:190px"><div class="card-icon"><svg width="30" height="30"><use href="#ico-building"/></svg></div><div class="card-title">Building &amp;<br>Pest Inspections</div></div>
  <div class="abs card" style="left:823px;top:190px"><div class="card-icon"><svg width="30" height="30"><use href="#ico-building"/></svg></div><div class="card-title">Building &amp;<br>Pest Inspections</div></div>

  <div class="abs card" style="left:181px;top:353px"><div class="card-icon"><svg width="30" height="30"><use href="#ico-building"/></svg></div><div class="card-title">Building &amp;<br>Pest Inspections</div></div>
  <div class="abs card" style="left:395px;top:353px"><div class="card-icon"><svg width="30" height="30"><use href="#ico-building"/></svg></div><div class="card-title">Building &amp;<br>Pest Inspections</div></div>
  <div class="abs card" style="left:609px;top:353px"><div class="card-icon"><svg width="30" height="30"><use href="#ico-building"/></svg></div><div class="card-title">Building &amp;<br>Pest Inspections</div></div>
  <div class="abs card" style="left:823px;top:353px"><div class="card-icon"><svg width="30" height="30"><use href="#ico-building"/></svg></div><div class="card-title">Building &amp;<br>Pest Inspections</div></div>

  <div class="abs btn btn-yellow" style="left:547px;top:527px;width:106px">View All Services</div>
</section>
<div class="abs divider" style="top:589px"></div>

<!-- Consultations -->
<section>
  <div class="abs photo" role="img" aria-label="Inspector in orange hard hat and colleague in white hard hat pointing at a brick wall" style="left:181px;top:628px;width:337px;height:344px"></div>
  <div class="abs photo-alt framed" role="img" aria-label="Two inspectors in hard hats reviewing plans beside brick walls on site" style="left:256px;top:815px;width:314px;height:207px"></div>

  <div class="abs eyebrow" style="left:608px;top:712px">22 Years Experience</div>
  <h2 class="abs heading" style="left:608px;top:731px">Korvenna Offers Consultations to Support.</h2>
  <div class="abs rule" style="left:608px;top:764px"></div>
  <p class="abs para" style="left:608px;top:793px;width:410px">With over 22 years of industry experience, our expert team delivers exceptional, efficient, and innovative solutions tailored to your project needs. Committed to client satisfaction, we build lasting relationships based on integrity, trust, and transparency.</p>
  <p class="abs para" style="left:608px;top:853px;width:410px">Korvenna offers consultations to support how our expertise can turn your project visions into a reality.</p>
  <div class="abs btn btn-dark" style="left:608px;top:911px;width:105px">View All Services</div>
  <div class="abs wordmark" style="left:606px;top:993px">KORVENNA</div>
</section>

<!-- Vision -->
<section>
  <div class="abs eyebrow" style="left:181px;top:1154px">South East Queensland</div>
  <h2 class="abs heading" style="left:181px;top:1173px">Our Vision Is To Be The Foremost Company.</h2>
  <div class="abs rule" style="left:181px;top:1206px"></div>
  <p class="abs para" style="left:181px;top:1235px;width:405px">At Korvenna Australia Pty Ltd, our vision is to be the foremost construction company in South East Queensland, renowned for our unparalleled expertise.</p>
  <p class="abs para" style="left:181px;top:1280px;width:405px">We aim to lead the industry by delivering integrated, specialized services across building &amp; pest inspections, estimating, project management, and construction management.</p>
  <div class="abs btn btn-dark" style="left:181px;top:1337px;width:105px">View All Services</div>
  <div class="abs wordmark" style="left:392px;top:1428px">KORVENNA</div>

  <div class="abs photo" role="img" aria-label="Inspector in orange hard hat and colleague in white hard hat pointing at a brick wall" style="left:682px;top:1062px;width:337px;height:344px"></div>
  <div class="abs photo-alt framed" role="img" aria-label="Two inspectors in hard hats reviewing plans beside brick walls on site" style="left:632px;top:1249px;width:314px;height:207px"></div>
</section>

<!-- Stats -->
<section>
  <div class="abs stats-band" role="img" aria-label="Blurred dark photo of construction workers in hard hats"></div>
  <div class="abs eyebrow" style="left:181px;top:1593px">You Need To Know</div>
  <h2 class="abs heading" style="left:181px;top:1612px;color:var(--white)">Few Fun Fact About Korvenna</h2>
  <div class="abs rule" style="left:181px;top:1644px"></div>
  <p class="abs para" style="left:181px;top:1674px;width:200px;color:var(--white)">We want people to thrive at Korvenna we believe you do your best work when you feel your best. Here are a just a few benefits we're proud to provide our team.</p>
  <div class="abs stat" style="left:444px;top:1595px"><div class="stat-num">22+</div><div class="stat-label">Years Experience</div></div>
  <div class="abs stat" style="left:644px;top:1595px"><div class="stat-num">1,200+</div><div class="stat-label">Completed Projects</div></div>
  <div class="abs stat" style="left:844px;top:1595px"><div class="stat-num">300+</div><div class="stat-label">Happy Clients</div></div>
</section>

<!-- Why choose us -->
<section>
  <svg class="abs" style="left:210px;top:1904px" width="300" height="355" aria-hidden="true">
    <polygon points="6,0 210,0 204,17 0,17" fill="#fdb913"/>
    <polygon points="86,337 290,337 284,354 80,354" fill="#fdb913"/>
  </svg>
  <div class="abs photo" role="img" aria-label="Inspector in orange hard hat with smiling colleague in white hard hat holding plans" style="left:181px;top:1921px;width:354px;height:320px"></div>
  <div class="abs badge" style="left:479px;top:2034px">Korvenna</div>

  <div class="abs eyebrow" style="left:619px;top:1868px">Why Choose Us ?</div>
  <h2 class="abs heading" style="left:619px;top:1887px;width:400px">With <span style="color:var(--yellow);font-weight:500">Korvenna Australia</span>, you gain peace of mind knowing that your property is safe, sound, and compliant.</h2>
  <div class="abs rule" style="left:619px;top:1935px"></div>
  <p class="abs para" style="left:619px;top:1966px;width:400px">Unlike tick-a-flick inspectors who rush through checklists, our inspections are conducted by a seasoned builder with over 22 years of hands-on industry experience and a keen eye for detail. We uphold the highest quality standards, ensuring no detail is overlooked.</p>
  <p class="abs para" style="left:619px;top:2026px;width:400px">Our expert takes genuine pride in his work, meticulously assessing every aspect of a property with the same care and diligence he would for his own projects. We don't just identify issues we provide clear, actionable insights to help you make informed decisions with confidence.</p>
  <ul class="abs bullets" style="left:619px;top:2090px;width:405px">
    <li>Industry Expertise – Our inspectors bring over 22 years of hands-on experience.</li>
    <li>Advanced Technology – We leverage state-of-the-art tools for precise assessments.</li>
    <li>Useful Reports – Receive clear, easy-to-understand findings with actionable insights.</li>
    <li>Fast Turnaround – Get reports quickly to make informed decisions.</li>
    <li>Customer-Focused – Providing tailored advice to help you navigate inspection findings.</li>
  </ul>
  <p class="abs para" style="left:619px;top:2211px;width:400px">Buying, selling, building, or investing? Let Korvenna Australia simplify the process. Contact us today to discuss your project and discover the expertise that makes us industry leaders.</p>
  <div class="abs btn btn-yellow" style="left:619px;top:2267px;width:109px">Contact Us Today</div>
</section>

<!-- Partners -->
<section>
  <div class="abs partners-band"></div>
  <div class="abs partner" style="left:181px;top:2428px">Tarvell Structures</div>
  <div class="abs partner" style="left:352px;top:2428px">Tarvell Structures</div>
  <div class="abs partner" style="left:524px;top:2428px">Tarvell Structures</div>
  <div class="abs partner" style="left:695px;top:2428px">Tarvell Structures</div>
  <div class="abs partner" style="left:867px;top:2428px">Tarvell Structures</div>
  <div class="abs dot" style="left:584px;top:2535px"></div>
  <div class="abs dot on" style="left:597px;top:2535px"></div>
  <div class="abs dot" style="left:610px;top:2535px"></div>
</section>

<!-- Call to action -->
<section>
  <div class="abs cta"></div>
  <div class="abs" style="left:218px;top:2632px;font-size:9.5px;font-weight:500;color:var(--white)">Dont Waste Your Time!</div>
  <div class="abs heading" style="left:218px;top:2650px">Get an Inspecton Today!</div>
  <div class="abs" style="left:402px;top:2622px;width:2px;height:56px;background:var(--white)"></div>
  <p class="abs para" style="left:442px;top:2627px;width:390px;color:var(--ink)">Submit a request online today to arrange a top rated building expert. We're always ready to assist with queries, offer a quote, and keep your property safe and compliant. Gain confidence with expert inspections across Australia.</p>
  <div class="abs btn btn-dark" style="left:876px;top:2632px;width:106px">Contact Us Now</div>
</section>

<!-- Footer -->
<footer>
  <div class="abs f-label" style="left:181px;top:2755px">Phone</div>
  <div class="abs f-value" style="left:181px;top:2774px">+61 400 582 916</div>
  <div class="abs f-label" style="left:367px;top:2755px">Email</div>
  <div class="abs f-value" style="left:367px;top:2774px">info@korvennaaustralia.com.au</div>
  <div class="abs f-label" style="left:619px;top:2755px">Address</div>
  <div class="abs f-value" style="left:619px;top:2774px">PO Box 88, Wavell Park, Q, 4090, Australia</div>
  <div class="abs f-label" style="left:892px;top:2755px">Follow Us</div>
  <div class="abs f-value" style="left:892px;top:2774px">Social Feed, Photo Feed, Clips</div>
  <div class="abs divider" style="top:2827px"></div>
  <div class="abs copyright" style="top:2849px">© Copyright 2025 Korvenna Australia | Brellwick Studio.</div>
</footer>

</body>
</html>
```